Restaurant menu design

I need a menu for a restaurant in Spain.
It has to be bohemian but modern. We need something romantic and elegant.
The restaurant is elegant with good food and an excellent reputation. It is also modern at the same time.
The restaurant is superbly decorated and very chick so we need something "class" to fit in with the surroundings.
The size of the document must be 325 mm in high and 245 mm as a maximum and preferably made in indesign.

Reason: Thank you all for your designs.
So far all your designs are ok but it isn´t what we are looking for. Most of the designs are too loaded, too many colors and too much decoration.

Target Market(s)

Adults of various age groups and different nationalities mostly European.

Industry/Entity Type

Restaurant

Requirements
Must have
• The menu must have two interior pages with the text as in the document attached.It must be easily legible.
Nice to have
• See what kind of menus they use in important restaurants in places like Paris, see what designs are in trend, but Not necessarily doing the same style if it doesn’t fit in with the description above.
Should not have
• Nothing old fashioned.

```html
<!DOCTYPE html>
<html lang="es">
<head>
<meta charset="utf-8">
<title>La Rêverie · Carta</title>
<link href="https://fonts.googleapis.com/css2?family=Parisienne&family=Tinos:ital@1&display=swap" rel="stylesheet">
<style>
:root{
  --plum:#a95a7e;
  --blush:#fbd7df;
  --paper:#fff2f4;
  --outer:#fdf1f3;
  --title:#9e2a33;
  --ink:#1e1a1c;
}
*{margin:0;padding:0;box-sizing:border-box}
html,body{width:1200px;height:796px;overflow:hidden;background:var(--outer)}
.menu{position:relative;width:1200px;height:796px;font-family:'Tinos',serif;font-style:italic;color:var(--ink)}
.band-top{position:absolute;left:0;top:28px;width:1200px;height:25px;background:var(--plum)}
.bar{position:absolute;top:0;width:26px;height:796px;background:var(--plum)}
.bar-left{left:28px}.bar-right{left:1146px}
.frame{position:absolute;left:54px;top:53px;width:1092px;height:743px;background:var(--blush)}
.sheet{position:absolute;left:81px;top:82px;width:1038px;height:714px;background:var(--paper)}
.section{position:absolute}
.section-title{font-family:'Parisienne',cursive;font-style:normal;font-weight:400;color:var(--title);font-size:30px;text-align:center;line-height:1}
.items{list-style:none;font-size:11.6px}
.item{display:flex;align-items:baseline;white-space:nowrap}
.item .name{flex:none}
.item .dots{flex:1;border-bottom:1px dotted #555;margin:0 2px;transform:translateY(-3px)}
.item .price{flex:none;font-size:9.6px}
.item .note{display:block;font-size:7.2px;margin-top:1px}
.item.two-line{align-items:flex-end}
.salsas{position:absolute;left:631px;top:430px;width:463px;height:37px;border:1px solid #888;display:flex;align-items:center;justify-content:center;gap:6px;font-size:9.5px}
.salsas .label{font-family:'Parisienne',cursive;font-style:normal;color:var(--title);font-size:15px}
.salsas .amt{font-size:8px;margin:0 4px 0 8px}
</style>
</head>
<body>
<div class="menu">
  <div class="band-top"></div>
  <div class="bar bar-left"></div>
  <div class="bar bar-right"></div>
  <div class="frame"></div>
  <div class="sheet"></div>

  <section class="section" style="left:115px;top:100px;width:454px">
    <h2 class="section-title">Entradas</h2>
    <ul class="items" style="margin-top:26px;line-height:17.3px">
      <li class="item"><span class="name">Ensalada La Rêverie. Lechuga, tomate</span><span class="dots"></span><span class="price">7,75 €</span></li>
      <li class="item"><span class="name">Ensalada Caprese (Tomate y Mozzarella)</span><span class="dots"></span><span class="price">7,75 €</span></li>
      <li class="item"><span class="name">Escarola al Queso de Cabra con Bacon</span><span class="dots"></span><span class="price">6,75 €</span></li>
      <li class="item"><span class="name">Cocktail de Gambas, Langostinos y Aguacate</span><span class="dots"></span><span class="price">7,50 €</span></li>
      <li class="item"><span class="name">La Sopa de Pescado</span><span class="dots"></span><span class="price">8,25 €</span></li>
      <li class="item"><span class="name">Crema de Espárragos Trigueros y Calabacín</span><span class="dots"></span><span class="price">5,95 €</span></li>
      <li class="item"><span class="name">Carpaccio de Ternera</span><span class="dots"></span><span class="price">11,50 €</span></li>
      <li class="item"><span class="name">Carpaccio de Salmón al Eneldo</span><span class="dots"></span><span class="price">9,75 €</span></li>
      <li class="item"><span class="name">Carpaccio de Atún</span><span class="dots"></span><span class="price">13,95 €</span></li>
      <li class="item"><span class="name">Melón con Jamón Ibérico</span><span class="dots"></span><span class="price">9,25 €</span></li>
      <li class="item"><span class="name">Parrillada de Verduras</span><span class="dots"></span><span class="price">7,95 €</span></li>
      <li class="item"><span class="name">Parrillada de Verduras Gratinada al Queso de Cabra</span><span class="dots"></span><span class="price">8,95 €</span></li>
      <li class="item"><span class="name">Gambas Roja de la Bahía</span><span class="dots"></span><span class="price">12,95 €</span></li>
    </ul>
  </section>

  <section class="section" style="left:115px;top:426px;width:454px">
    <h2 class="section-title" style="margin-left:-6px">Pescados al Grill</h2>
    <ul class="items" style="margin-top:28px;line-height:17.3px">
      <li class="item"><span class="name">Lubina al Hinojo.</span><span class="dots"></span><span class="price">15,50 €</span></li>
      <li class="item"><span class="name">Lubina Fileteada y su Salsa Rústica con Berenjena</span><span class="dots"></span><span class="price">18,50 €</span></li>
      <li class="item"><span class="name">Filete de Rodaballo y su Salsa de Marisco</span><span class="dots"></span><span class="price">17,25 €</span></li>
      <li class="item"><span class="name">Dorada del Mediterráneo</span><span class="dots"></span><span class="price">13,95 €</span></li>
      <li class="item"><span class="name">Lenguado al Grill con Hierbas Provenzales</span><span class="dots"></span><span class="price">20,75 €</span></li>
      <li class="item"><span class="name">Pieza de Atún Fresco y su Salsa Griega</span><span class="dots"></span><span class="price">18,95 €</span></li>
      <li class="item"><span class="name">Lomo de Salmón con Salsa de Frambuesa</span><span class="dots"></span><span class="price">11,25 €</span></li>
      <li class="item"><span class="name">Parrillada de Pescado y Marisco</span><span class="dots"></span><span class="price">23,505 €</span></li>
    </ul>
  </section>

  <section class="section" style="left:120px;top:655px;width:455px">
    <h2 class="section-title" style="margin-left:-6px">Especial Niños</h2>
    <ul class="items" style="margin-top:27px;line-height:17.3px">
      <li class="item"><span class="name">Solomillo Junior, huevo y patatas fritas</span><span class="dots"></span><span class="price">6,25 €</span></li>
      <li class="item"><span class="name">Fish &amp; chips</span><span class="dots"></span><span class="price">6,25 €</span></li>
    </ul>
  </section>

  <section class="section" style="left:629px;top:100px;width:466px">
    <h2 class="section-title">Carnes</h2>
    <ul class="items" style="margin-top:25px;line-height:19px">
      <li class="item"><span class="name">Pechuga de Pollo “Madame Rose” con Champiñones y Bacon</span><span class="dots"></span><span class="price">11,95 €</span></li>
      <li class="item"><span class="name">Chuletas de Cordero</span><span class="dots"></span><span class="price">14,50 €</span></li>
      <li class="item"><span class="name">Costillas de Cerdo con Salsa Barbacoa</span><span class="dots"></span><span class="price">9,95 €</span></li>
      <li class="item"><span class="name">Paletilla de Cordero Lechal</span><span class="dots"></span><span class="price">19,75 €</span></li>
      <li class="item"><span class="name">Le Strogonoff. Finas tiras de Solomillo con su Salsa de Champiñones</span><span class="dots"></span><span class="price">15,90 €</span></li>
      <li class="item"><span class="name">Solomillo de Ternera</span><span class="dots"></span><span class="price">18,50 €</span></li>
      <li class="item"><span class="name">Solomillo de Ternera a la Ibérica con Jamón Ibérico y Ligera Salsa de Vino Tinto</span><span class="dots"></span><span class="price">20,75 €</span></li>
      <li class="item two-line" style="line-height:13px;padding:3px 0 2px"><span class="name">“Hamburger Royal Steak Hachè”<span class="note">&nbsp;Picata de Solomillo de Ternera, Huevo Frito y Patatas Fritas</span></span><span class="dots"></span><span class="price">14,50 €</span></li>
      <li class="item"><span class="name">Solomillo de Cerdo al Horno con Bacon y su Salsa de Setas</span><span class="dots"></span><span class="price">14,25 €</span></li>
      <li class="item"><span class="name">Entrecôte de Ternera</span><span class="dots"></span><span class="price">14,75 €</span></li>
      <li class="item"><span class="name">T-Bone Steak de Ternera</span><span class="dots"></span><span class="price">16,75 €</span></li>
      <li class="item"><span class="name">Chuletón de Ternera</span><span class="dots"></span><span class="price">20,25 €</span></li>
      <li class="item"><span class="name">Parrillada de Carnes y Embutidos</span><span class="dots"></span><span class="price">21,50 €</span></li>
    </ul>
  </section>

  <div class="salsas">
    <span class="label">Salsas:</span>
    <span>Pimienta.</span><span class="amt">2,85 €</span>·
    <span>Roquefort.</span><span class="amt">2,95 €</span>·
    <span>Bearnaise.</span><span class="amt">2,95 €</span>·
    <span>de Champiñones.</span><span class="amt">2,65 €</span>
  </div>

  <section class="section" style="left:629px;top:502px;width:466px">
    <h2 class="section-title">Las Delicias de la Rêverie</h2>
    <ul class="items" style="margin-top:27px;line-height:19px">
      <li class="item"><span class="name">Frambuesas “La Rêverie”</span><span class="dots"></span><span class="price">6,25 €</span></li>
      <li class="item"><span class="name">Cocktail de Frutas Exóticas</span><span class="dots"></span><span class="price">5,25 €</span></li>
      <li class="item"><span class="name">Sorbete de Limón, Coulis de Fresa y Vodka</span><span class="dots"></span><span class="price">5,50 €</span></li>
      <li class="item"><span class="name">Pastel de Chocolate Casero con su Salsa de Vainilla</span><span class="dots"></span><span class="price">6,25 €</span></li>
      <li class="item"><span class="name">Crême Brulée</span><span class="dots"></span><span class="price">6,25 €</span></li>
      <li class="item"><span class="name">Tarta de Manzana Casera “Tatín” y su Helado de Vainilla</span><span class="dots"></span><span class="price">6,95 €</span></li>
      <li class="item"><span class="name">Copa Glaciale</span><span class="dots"></span><span class="price">6,75 €</span></li>
      <li class="item"><span class="name">Pera al Chocolate Caliente y Helado de Macadamia</span><span class="dots"></span><span class="price">5,95 €</span></li>
      <li class="item"><span class="name">Tarta de Queso con Coulis de Fresa</span><span class="dots"></span><span class="price">5,75 €</span></li>
      <li class="item"><span class="name">Nuestra Mousse de Chocolate</span><span class="dots"></span><span class="price">5,75 €</span></li>
    </ul>
  </section>
</div>
</body>
</html>
```